Auto Tuning Shop needs an advertising design

An advertising design that can be used online for marketing on Facebook, Google, Instagram. A picture that says exactly what we do - window tinting / car window films. Looks professional and is informative. But not too much content and text.
Possibly a picture of the car looks like window tint from the outside (very dark), but when sitting in the car you have a perfect view of the outside.
Passwords in picture: UV protection, heat protection, burglary protection, privacy protection
Not too many colors.

Here are a few sample pictures as we often designed it ourselves, but it has to look more professional.

Target Market(s)

Reach new customers because it is a campaign / offer

Requirements
Must have
• German language
Nice to have
• Passwords in picture: UV protection, heat protection, burglary protection, privacy protection

```html
<!DOCTYPE html>
<html lang="de">
<head>
<meta charset="utf-8">
<title>Veltra – Professionelle Scheibentönung</title>
<link rel="stylesheet" href="https://fonts.googleapis.com/css2?family=Lato:wght@400;700&family=Oswald:wght@600&display=swap">
<style>
  :root {
    --page: #cfcfd1;
    --ink: #0c0c0c;
    --charcoal: #2b2b2d;
    --red: #e3212a;
    --red-deep: #8e1a1c;
    --gold: #d4b23c;
    --gold-light: #e9d27a;
    --silver: #c9c9c9;
    --white: #ffffff;
  }
  html, body {
    margin: 0;
    width: 1200px;
    height: 1200px;
    overflow: hidden;
    background: var(--page);
  }
  .banner {
    position: absolute;
    left: 40px;
    top: 258px;
    width: 1120px;
    height: 684px;
    box-shadow: 0 10px 24px rgba(0,0,0,.35);
  }
  .title { font-family: "Oswald", "Arial Narrow", sans-serif; font-weight: 600; fill: var(--white); }
  .subtitle { font-family: "Lato", Arial, sans-serif; font-weight: 700; fill: var(--white); }
  .brand { font-family: "Lato", Arial, sans-serif; font-weight: 700; fill: var(--red); }
  .contact-head { font-family: "Lato", Arial, sans-serif; font-weight: 700; fill: var(--red-deep); }
  .contact-line { font-family: "Lato", Arial, sans-serif; font-weight: 400; fill: var(--white); }
  .web { font-family: "Lato", Arial, sans-serif; font-weight: 700; fill: var(--ink); }
  .feature { font-family: "Lato", Arial, sans-serif; font-weight: 700; fill: var(--white); }
  .icon-gold { fill: none; stroke: var(--gold); stroke-width: 1.6; }
  .feature-icon { fill: var(--ink); }
</style>
</head>
<body>
<svg class="banner" viewBox="0 0 1013 619" xmlns="http://www.w3.org/2000/svg">
  <defs>
    <linearGradient id="headerBar" x1="0" y1="0" x2="0" y2="1">
      <stop offset="0" stop-color="#3a3a3c"/>
      <stop offset="1" stop-color="#1a1a1b"/>
    </linearGradient>
    <linearGradient id="subBar" x1="0" y1="0" x2="1" y2="0">
      <stop offset="0" stop-color="#1c0b0b"/>
      <stop offset=".55" stop-color="#8e1a1c"/>
      <stop offset="1" stop-color="#e3212a"/>
    </linearGradient>
    <linearGradient id="exteriorPhoto" x1="0" y1="0" x2="1" y2="1">
      <stop offset="0" stop-color="#c9d3dc"/>
      <stop offset=".28" stop-color="#4a4f55"/>
      <stop offset="1" stop-color="#16181b"/>
    </linearGradient>
    <linearGradient id="interiorPhoto" x1="0" y1="0" x2="1" y2="0">
      <stop offset="0" stop-color="#6f9a4d"/>
      <stop offset=".45" stop-color="#3d5c3a"/>
      <stop offset=".7" stop-color="#1d2430"/>
      <stop offset="1" stop-color="#4f7a44"/>
    </linearGradient>
    <linearGradient id="featurePanel" x1="0" y1="0" x2="1" y2="0">
      <stop offset="0" stop-color="#262628"/>
      <stop offset=".45" stop-color="#3a2627"/>
      <stop offset="1" stop-color="#c8262c"/>
    </linearGradient>
    <linearGradient id="tile" x1="0" y1="0" x2="1" y2="1">
      <stop offset="0" stop-color="#e4e4e4"/>
      <stop offset="1" stop-color="#9a9a9a"/>
    </linearGradient>
    <linearGradient id="webBar" x1="0" y1="0" x2="1" y2="0">
      <stop offset="0" stop-color="#e9d27a"/>
      <stop offset=".6" stop-color="#c9a22f"/>
      <stop offset="1" stop-color="#c9a22f" stop-opacity="0"/>
    </linearGradient>
  </defs>

  <!-- base -->
  <rect class="canvas-base" width="1013" height="619" fill="var(--ink)"/>

  <!-- diagonal red stripe -->
  <polygon class="stripe" points="235,0 396,0 621,372 483,372" fill="var(--red)"/>

  <!-- header -->
  <polygon class="header-bar" points="256,0 1013,0 1013,86 308,86" fill="url(#headerBar)"/>
  <rect class="header-rule" x="300" y="84" width="713" height="3" fill="var(--gold)"/>
  <text class="title" x="344" y="67" font-size="54" textLength="640" lengthAdjust="spacingAndGlyphs">PROFESSIONELLE SCHEIBENTÖNUNG</text>
  <polygon class="subtitle-bar" points="455,88 1013,88 1013,135 484,135" fill="url(#subBar)"/>
  <text class="subtitle" x="983" y="122" font-size="26" text-anchor="end">German Quality of Window</text>

  <!-- brand -->
  <circle class="brand-dot" cx="52" cy="70" r="14" fill="var(--red)"/>
  <text class="brand" x="76" y="82" font-size="36">VELTRA</text>

  <!-- photos -->
  <polygon class="photo-exterior" role="img" aria-label="Foto: dunkel getönte Autoscheibe von außen mit Regentropfen" points="0,160 343,160 483,372 0,372" fill="url(#exteriorPhoto)"/>
  <polygon class="photo-interior" role="img" aria-label="Foto: Blick aus dem Fahrzeuginneren durch die getönte Scheibe auf grüne Bäume" points="493,160 1013,160 1013,372 621,372" fill="url(#interiorPhoto)"/>

  <!-- bottom section -->
  <polygon class="stripe-lower" points="300,372 1013,372 1013,619 448,619" fill="var(--red)"/>
  <polygon class="feature-panel" points="470,375 1013,375 1013,619 610,619" fill="url(#featurePanel)"/>
  <rect class="divider" x="0" y="372" width="1013" height="3" fill="var(--gold)"/>

  <!-- contact -->
  <polygon class="contact-tab" points="43,374 300,374 332,422 75,422" fill="var(--gold)"/>
  <text class="contact-head" x="92" y="410" font-size="28">CONTACT:</text>

  <g class="contact-icons">
    <path class="icon-gold" d="M73 450 q-2 6 4 12 q6 5 9 3 l2-3 -4-3 -2 2 q-4-2-5-6 l2-1 -2-5z"/>
    <path d="M80 473 a6 6 0 0 1 12 0 c0 5 -6 11 -6 11 c0 0 -6 -6 -6 -11z" fill="var(--gold)"/>
    <circle cx="86" cy="473" r="2.2" fill="var(--ink)"/>
    <rect class="icon-gold" x="72" y="522" width="15" height="10"/>
    <path class="icon-gold" d="M72 522 l7.5 6 7.5-6"/>
  </g>
  <text class="contact-line" x="95" y="463" font-size="19">0151 20486 915</text>
  <text class="contact-line" x="95" y="487" font-size="19">Lindenweg 14,</text>
  <text class="contact-line" x="95" y="511" font-size="19">85716 München - Eching</text>
  <text class="contact-line" x="95" y="535" font-size="19">info@veltra-folie.de</text>

  <!-- website bar -->
  <rect class="web-red" x="0" y="565" width="90" height="35" fill="var(--red)"/>
  <rect class="web-gold" x="90" y="565" width="400" height="35" fill="url(#webBar)"/>
  <g class="globe" fill="none" stroke="var(--white)" stroke-width="1.5">
    <circle cx="70" cy="583" r="8"/>
    <ellipse cx="70" cy="583" rx="3.5" ry="8"/>
    <path d="M62 583h16"/>
  </g>
  <text class="web" x="95" y="591" font-size="21">www.veltra-folie.de</text>

  <!-- features -->
  <g class="feature-rules" stroke="#7a7a7a" stroke-width="1.2">
    <line x1="528" y1="441" x2="1005" y2="441"/>
    <line x1="560" y1="496" x2="1005" y2="496"/>
    <line x1="592" y1="552" x2="1005" y2="552"/>
  </g>

  <g class="feature-row">
    <polygon points="436,389 500,389 528,437 464,437" fill="url(#tile)"/>
    <circle cx="483" cy="403" r="7" fill="none" stroke="var(--ink)" stroke-width="1.5"/>
    <text x="483" y="406" font-family="Lato, sans-serif" font-size="7" font-weight="700" text-anchor="middle" class="feature-icon">UV</text>
    <rect class="feature-icon" x="468" y="414" width="22" height="4"/>
    <rect class="feature-icon" x="468" y="421" width="22" height="4"/>
    <text class="feature" x="558" y="423" font-size="30">UV-Schutz</text>
  </g>

  <g class="feature-row">
    <polygon points="468,444 532,444 560,492 496,492" fill="url(#tile)"/>
    <circle class="feature-icon" cx="514" cy="468" r="8"/>
    <g stroke="var(--ink)" stroke-width="2.2" stroke-linecap="round">
      <line x1="514" y1="452" x2="514" y2="456"/><line x1="514" y1="480" x2="514" y2="484"/>
      <line x1="498" y1="468" x2="502" y2="468"/><line x1="526" y1="468" x2="530" y2="468"/>
      <line x1="503" y1="457" x2="506" y2="460"/><line x1="522" y1="476" x2="525" y2="479"/>
      <line x1="525" y1="457" x2="522" y2="460"/><line x1="506" y1="476" x2="503" y2="479"/>
    </g>
    <text class="feature" x="598" y="478" font-size="30">Hitzeschutz</text>
  </g>

  <g class="feature-row">
    <polygon points="500,500 564,500 592,548 528,548" fill="url(#tile)"/>
    <path class="feature-icon" d="M546 510 l14 5 v8 c0 9 -6 14 -14 17 c-8 -3 -14 -8 -14 -17 v-8z"/>
    <path d="M538 524 q8 -7 16 0 q-8 7 -16 0z" fill="var(--silver)"/>
    <circle class="feature-icon" cx="546" cy="524" r="2.5"/>
    <text class="feature" x="625" y="534" font-size="30">Datenschutz</text>
  </g>

  <g class="feature-row">
    <polygon points="531,555 595,555 623,603 559,603" fill="url(#tile)"/>
    <path d="M571 575 v-5 a7 7 0 0 1 14 0 v5" fill="none" stroke="var(--ink)" stroke-width="3"/>
    <rect class="feature-icon" x="567" y="575" width="22" height="18" rx="2"/>
    <circle cx="578" cy="583" r="2.5" fill="var(--silver)"/>
    <text class="feature" x="656" y="589" font-size="30">Einbruchschutz</text>
  </g>
</svg>
</body>
</html>
```